Copperleaf Motorized Shade Business Card

Hello, we've had our logo made. Now we are looking for a clean and cool looking business card. One side can just be the logo with any design elements that might look good with it. The other side will be Name, Phone Number and Email. There will not be an address on the card.

```html
<!DOCTYPE html>
<html lang="en">
<head>
<meta charset="utf-8">
<title>Copperleaf Motorized Shades – Business Card</title>
<link href="https://fonts.googleapis.com/css2?family=Oswald:wght@500;600&family=Open+Sans:wght@400;600&display=swap" rel="stylesheet">
<style>
  :root {
    --navy: #0d3b7a;
    --sky: #29a8e0;
    --white: #ffffff;
    --text-grey: #555b66;
    --backdrop: #e9ebee;
  }
  * { box-sizing: border-box; margin: 0; padding: 0; }
  html, body { width: 1200px; height: 870px; overflow: hidden; }
  body {
    background: var(--backdrop);
    font-family: "Open Sans", Arial, sans-serif;
    position: relative;
  }
  .card {
    position: absolute;
    top: 280px;
    width: 540px;
    height: 310px;
    border-radius: 14px;
    overflow: hidden;
    box-shadow: 0 6px 18px rgba(0,0,0,0.12);
  }
  .card--front { left: 40px; background: var(--white); }
  .card--back { left: 620px; background: var(--navy); }

  .wordmark {
    font-family: "Oswald", Arial, sans-serif;
    font-weight: 600;
    text-transform: uppercase;
    display: flex;
    align-items: center;
    gap: 10px;
  }
  .wordmark__square {
    width: 34px; height: 34px;
    flex: none;
  }
  .wordmark__text { line-height: 1; }
  .wordmark__name { display: block; font-size: 34px; letter-spacing: 0.5px; }
  .wordmark__tag { display: block; font-size: 12.5px; letter-spacing: 2.6px; margin-top: 4px; }

  .card--front .wordmark { position: absolute; left: 24px; top: 92px; color: var(--navy); }
  .card--front .wordmark__square { background: var(--navy); }

  .divider {
    position: absolute;
    left: 272px; top: 58px;
    width: 1px; height: 140px;
    background: var(--sky);
  }
  .contact-block { position: absolute; left: 296px; top: 56px; }
  .person__name {
    font-family: "Oswald", Arial, sans-serif;
    font-weight: 500;
    font-size: 19px;
    color: var(--navy);
    text-transform: uppercase;
    letter-spacing: 0.3px;
  }
  .person__role { font-size: 12px; color: var(--text-grey); margin-top: 2px; }
  .contact-list { list-style: none; margin-top: 26px; }
  .contact-list li {
    display: flex; align-items: center; gap: 10px;
    font-size: 12px; color: var(--text-grey);
    margin-bottom: 9px;
  }
  .contact-list svg { width: 18px; height: 18px; flex: none; }
  .contact-list .web-strong { color: var(--navy); font-weight: 600; }

  .front-wave { position: absolute; left: 0; bottom: 0; width: 540px; height: 80px; }

  .card--back .wordmark {
    position: absolute; left: 0; right: 0; top: 106px;
    justify-content: center; color: var(--white);
  }
  .card--back .wordmark__square { background: var(--white); }
  .back-web {
    position: absolute; left: 0; right: 0; top: 232px;
    text-align: center; font-size: 12.5px; letter-spacing: 1.2px;
    color: var(--sky);
  }
  .back-web strong { color: var(--white); font-weight: 600; }
</style>
</head>
<body>

<section class="card card--front" aria-label="Business card front">
  <div class="wordmark">
    <span class="wordmark__square"></span>
    <span class="wordmark__text">
      <span class="wordmark__name">Copperleaf</span>
      <span class="wordmark__tag">Motorized Shades</span>
    </span>
  </div>

  <div class="divider"></div>

  <div class="contact-block">
    <h1 class="person__name">Marisol Delgado</h1>
    <p class="person__role">Manager</p>
    <ul class="contact-list">
      <li>
        <svg viewBox="0 0 18 18" aria-hidden="true"><circle cx="9" cy="9" r="8" fill="none" stroke="#29a8e0" stroke-width="1.2"/><path d="M6.3 5.2l1.4-.3.8 1.9-1 .7c.5 1.1 1.3 1.9 2.4 2.4l.7-1 1.9.8-.3 1.4c-3.3.2-6.1-2.6-5.9-5.9z" fill="#29a8e0"/></svg>
        <span>+0408 311 672</span>
      </li>
      <li>
        <svg viewBox="0 0 18 18" aria-hidden="true"><circle cx="9" cy="9" r="8" fill="none" stroke="#29a8e0" stroke-width="1.2"/><rect x="5" y="6.2" width="8" height="5.6" fill="none" stroke="#29a8e0" stroke-width="1.1"/><path d="M5 6.2l4 3 4-3" fill="none" stroke="#29a8e0" stroke-width="1.1"/></svg>
        <span>info@copperleafmotorized.com</span>
      </li>
      <li>
        <svg viewBox="0 0 18 18" aria-hidden="true"><circle cx="9" cy="9" r="8" fill="#29a8e0"/><circle cx="9" cy="9" r="4.5" fill="none" stroke="#fff" stroke-width="1"/><path d="M4.5 9h9M9 4.5c-2 2.5-2 6.5 0 9M9 4.5c2 2.5 2 6.5 0 9" fill="none" stroke="#fff" stroke-width="0.9"/></svg>
        <span>www.<span class="web-strong">copperleafmotorized</span>.com</span>
      </li>
    </ul>
  </div>

  <svg class="front-wave" viewBox="0 0 540 80" preserveAspectRatio="none" aria-hidden="true">
    <path d="M0 40 C150 10 330 14 540 34 L540 80 L0 80 Z" fill="#29a8e0"/>
    <path d="M0 50 C150 20 330 26 540 42 L540 80 L0 80 Z" fill="#ffffff"/>
    <path d="M0 56 C160 28 340 34 540 50 L540 80 L0 80 Z" fill="#0d3b7a"/>
  </svg>
</section>

<section class="card card--back" aria-label="Business card back">
  <div class="wordmark">
    <span class="wordmark__square"></span>
    <span class="wordmark__text">
      <span class="wordmark__name">Copperleaf</span>
      <span class="wordmark__tag">Motorized Shades</span>
    </span>
  </div>
  <p class="back-web">www.<strong>copperleafmotorized</strong>.com</p>
</section>

</body>
</html>
```